Business Card Design Project

Business and Appointment Card for Medical Practice. On back of card we would like to have: blank line for patient name, Mon-Fri each with a check box next to the day, blank line for appointment date, blank line for appointment time, with option to circle am or pm.

Target Market(s)

Professional Business Associates, as well as function as patient appointment cards (on back side of card)

Industry/Entity Type

Business

Colors

Designer to choose colors to be used in the design.

```html
<!DOCTYPE html>
<html lang="en">
<head>
<meta charset="utf-8">
<title>Maple Grove Medical Associates – Business &amp; Appointment Card</title>
<link rel="stylesheet" href="https://fonts.googleapis.com/css2?family=Open+Sans:wght@400;600&display=swap">
<style>
  :root {
    --page-bg: #e9e9e9;
    --brand-green: #0b6b3a;
    --brand-green-deep: #085a30;
    --brand-maroon: #8e1b1f;
    --card-white: #ffffff;
    --ink-grey: #444444;
    --faint-grey: #ececec;
    --faint-grey-ring: #e2e2e2;
    --faint-green: #157a46;
    --faint-green-ring: #1c804e;
    --field-white: #ffffff;
  }
  * { box-sizing: border-box; margin: 0; padding: 0; }
  html, body { width: 1200px; height: 900px; overflow: hidden; }
  body {
    background: var(--page-bg);
    font-family: "Open Sans", sans-serif;
    position: relative;
  }
  .card {
    position: absolute;
    top: 295px;
    width: 540px;
    height: 310px;
    border-radius: 22px;
    background: var(--card-white);
    padding: 8px;
  }
  .card--front { left: 40px; }
  .card--back { left: 620px; }

  .card__frame {
    position: relative;
    width: 100%;
    height: 100%;
    border-radius: 16px;
    overflow: hidden;
  }
  .card--front .card__frame {
    border: 6px solid var(--brand-green);
    background: var(--card-white);
  }
  .card--back .card__frame {
    border: 3px solid var(--brand-green-deep);
    background: var(--brand-green);
  }

  .emblem-fade {
    position: absolute;
    border-radius: 50%;
  }
  .card--front .emblem-fade {
    width: 250px; height: 250px; right: -60px; top: 50px;
    background: radial-gradient(circle, #f3f3f3 0%, var(--faint-grey) 70%);
    border: 6px solid var(--faint-grey-ring);
  }
  .card--back .emblem-fade {
    width: 300px; height: 300px; left: 110px; top: -20px;
    background: radial-gradient(circle, #127645 0%, var(--faint-green) 70%);
    border: 6px solid var(--faint-green-ring);
  }

  /* Front */
  .brand-name {
    position: absolute;
    left: 20px; top: 70px;
    color: var(--brand-maroon);
    font-weight: 600;
    display: flex; align-items: center; gap: 8px;
  }
  .brand-name__mark {
    width: 14px; height: 14px; border-radius: 50%;
    background: var(--brand-maroon);
  }
  .brand-name__text { line-height: 1.15; }
  .brand-name__main { font-size: 24px; display: block; letter-spacing: 0.5px; text-transform: uppercase; }
  .brand-name__sub { font-size: 12px; letter-spacing: 2px; display: block; text-transform: uppercase; }

  .person { position: absolute; left: 20px; top: 146px; }
  .person__name { color: var(--brand-maroon); font-weight: 600; font-size: 15px; line-height: 1.3; }
  .person__title { color: var(--ink-grey); font-size: 10px; }

  .contact-list {
    position: absolute; left: 20px; top: 196px;
    list-style: none; color: var(--ink-grey); font-size: 12px; line-height: 17px;
  }
  .contact-list li { display: flex; align-items: center; gap: 5px; }
  .contact-list svg { width: 11px; height: 11px; fill: var(--brand-maroon); }

  /* Back */
  .appointment-title {
    position: absolute; left: 0; right: 0; top: 50px;
    text-align: center; color: #fff; font-weight: 600; font-size: 17px;
  }
  .appointment-row {
    position: absolute; left: 20px; right: 12px;
    display: flex; align-items: center; color: #fff; font-size: 16px;
  }
  .appointment-row--name { top: 92px; }
  .appointment-row--date { top: 134px; }
  .appointment-row--time { top: 176px; }
  .appointment-row__label { width: 58px; flex: none; }
  .appointment-row__field { background: var(--field-white); height: 28px; }
  .appointment-row--name .appointment-row__field { flex: 1; }
  .appointment-row--date .appointment-row__field,
  .appointment-row--time .appointment-row__field { width: 168px; flex: none; }
  .weekday-checks { display: flex; gap: 7px; margin-left: 8px; font-size: 10px; }
  .weekday-checks span { display: flex; align-items: center; gap: 3px; }
  .weekday-checks i { display: inline-block; width: 12px; height: 12px; background: var(--field-white); }
  .meridiem { margin-left: 10px; font-size: 12px; }
</style>
</head>
<body>

<section class="card card--front" aria-label="Business card front">
  <div class="card__frame">
    <div class="emblem-fade" role="img" aria-label="Faint practice emblem decoration"></div>

    <div class="brand-name">
      <span class="brand-name__mark"></span>
      <span class="brand-name__text">
        <span class="brand-name__main">Maple Grove</span>
        <span class="brand-name__sub">Medical Associates</span>
      </span>
    </div>

    <div class="person">
      <p class="person__name">Daniel Reyes</p>
      <p class="person__title">Manager</p>
    </div>

    <ul class="contact-list">
      <li><svg viewBox="0 0 24 24"><path d="M6.6 10.8a15 15 0 0 0 6.6 6.6l2.2-2.2c.3-.3.7-.4 1-.2 1.1.4 2.3.6 3.6.6.6 0 1 .4 1 1V20c0 .6-.4 1-1 1A17 17 0 0 1 3 4c0-.6.4-1 1-1h3.5c.6 0 1 .4 1 1 0 1.3.2 2.5.6 3.6.1.3 0 .7-.2 1z"/></svg>617-555-0142</li>
      <li><svg viewBox="0 0 24 24"><path d="M12 2a10 10 0 1 0 0 20 10 10 0 0 0 0-20zm0 2c1 1.3 1.8 3.3 2 6h-4c.2-2.7 1-4.7 2-6zM4.1 11h3.9c.1 2.3.6 4.3 1.4 5.9A8 8 0 0 1 4.1 11zm0-2a8 8 0 0 1 5.3-5.9C8.6 4.7 8.1 6.7 8 9zm5.9 2h4c-.2 2.7-1 4.7-2 6-1-1.3-1.8-3.3-2-6zm6 0h3.9a8 8 0 0 1-5.3 5.9c.8-1.6 1.3-3.6 1.4-5.9zm0-2c-.1-2.3-.6-4.3-1.4-5.9A8 8 0 0 1 19.9 9z"/></svg>www.maplegrovemed.com</li>
      <li><svg viewBox="0 0 24 24"><path d="M2 5h20v14H2zm2 2v.5l8 5 8-5V7zm0 2.8V17h16V9.8l-8 5z"/></svg>info@maplegrovemed.com</li>
      <li><svg viewBox="0 0 24 24"><path d="M12 3 2 12h3v8h5v-5h4v5h5v-8h3z"/></svg>120 Elm Street Boston</li>
    </ul>
  </div>
</section>

<section class="card card--back" aria-label="Appointment card back">
  <div class="card__frame">
    <div class="emblem-fade" role="img" aria-label="Faint practice emblem decoration"></div>

    <h2 class="appointment-title">Appointment</h2>

    <div class="appointment-row appointment-row--name">
      <span class="appointment-row__label">Name :</span>
      <span class="appointment-row__field"></span>
    </div>

    <div class="appointment-row appointment-row--date">
      <span class="appointment-row__label">Date &nbsp;:</span>
      <span class="appointment-row__field"></span>
      <span class="weekday-checks">
        <span>Mon <i></i></span>
        <span>Tue <i></i></span>
        <span>Wed <i></i></span>
        <span>Thu <i></i></span>
        <span>Fri <i></i></span>
      </span>
    </div>

    <div class="appointment-row appointment-row--time">
      <span class="appointment-row__label">Time &nbsp;:</span>
      <span class="appointment-row__field"></span>
      <span class="meridiem">am / pm</span>
    </div>
  </div>
</section>

</body>
</html>
```